Website template and forms
Velvet lantern
Website template and forms  - Financial Services
Creative Brief
Financial Services
http://www.velvet-lantern.co.uk
Velvet Lantern works as an intermediary between clients who are looking into products such as life insurance and the IFA and Brokerage community who can assist them.
We have teamed up with some of the countries largest survey companies and respond directly to customers who have suggested they may be interested in learning more.
General knowledge about life insurance and how it operates is limited within what the industry terms “the insurance gap” and our aim is to ensure our customers understand the products they are interested in and they feel the products are suitable for them.
Whilst we do not provide or offer advice at any time, we spend time talking with customers about their need for cover. We find a lot of our customers have made the decision that they need to have cover in place but have yet to think about how much cover they require and over what time period. This can cause difficulties when calling into brokerages directly or indeed when using comparison sites, where you are asked direct questions and are not always equipped with the answers. This can then be a frustrating process for all involved.
We have essentially two sets of customers, the customers who respond to surveys and whom we then call and assist and also the IFA/Brokerages with whom we place our leads.
We will only transfer a client to a brokerage when they have a good understanding of what they are looking for, often we can outline the areas to think about and arrange to call the client back. This works for everyone concerned as the buyer knows what they are looking for and understands what the product does and doesn’t do and also ensures that the commercial side of our business, which is lead provision maintains its reputation.
We have long term relationships with our clients and companies have chosen us as their sole partner for Life insurance transfers. We work continually on our approach and service so that brokerages receive those customers whom they feel they can benefit; taking daily feedback on every lead we supply to ensure standards are high.
Each brokerage has its own set of criteria and parameters for customers, for example IFA companies who like to advise clients need the customers to have enough time to spare to complete a fact find and have their needs assessed. Brokerages offer a quick and comprehensive service often finding customers much more competitive products than they would otherwise have access to.
Like : Exisiting logo. Dislikes: Flash, moving images, unindexable content
Colorful
Humorous
yellow
what ever works
Arial, Verdana, Trebuchet MS, Times New Roman, Century Gothic, Georgia
left side
please email derek@velvet-lantern.co.uk for the full design brief. We also need some auto email forms creating as part of the project. Please inform me if you cannot do this.

```html
<!DOCTYPE html>
<html lang="en">
<head>
<meta charset="utf-8">
<title>Velvet Lantern</title>
<link href="https://fonts.googleapis.com/css2?family=Arimo:wght@400;700&display=swap" rel="stylesheet">
<style>
:root{
  --blue:#2c6fb4;
  --blue-dark:#1d5796;
  --blue-light:#4a8fd0;
  --yellow:#ffd84a;
  --yellow-deep:#f4b000;
  --orange:#f0961c;
  --ink:#2b2b2b;
  --muted:#555b63;
  --hero-top:#ffffff;
  --hero-bottom:#e3e5e9;
  --band:#d3d5d9;
  --brand:#3d3f8c;
}
*{margin:0;padding:0;box-sizing:border-box}
html,body{width:1200px;height:1009px;overflow:hidden;background:#fff}
body{font-family:"Arimo",Arial,sans-serif;color:var(--ink);position:relative}
.abs{position:absolute}

.topbar{left:0;top:0;width:1200px;height:33px;background:#fff}
.follow{left:95px;top:5px;font-size:20px;color:var(--blue);display:flex;align-items:center;gap:6px}
.follow .social{width:20px;height:20px;background:var(--blue);border-radius:3px;display:inline-block}
.callus{left:820px;top:5px;font-size:20px;color:var(--blue);display:flex;align-items:center;gap:8px}
.callus .num{color:var(--orange)}

.nav{left:0;top:33px;width:1200px;height:54px;background:linear-gradient(var(--blue-light),var(--blue-dark));display:flex;padding-left:82px}
.nav a{color:#fff;text-decoration:none;font-size:17px;line-height:54px;padding:0 13px}
.nav a.active{background:linear-gradient(#ffd23a,var(--yellow-deep));color:var(--ink)}

.hero{left:0;top:87px;width:1200px;height:398px;background:linear-gradient(var(--hero-top),var(--hero-bottom))}
.mascot{left:100px;top:120px;width:150px;height:345px;border-radius:70px 70px 30px 30px;background:linear-gradient(#5fb4e8,#2b6fb6)}
.brand{left:252px;top:215px;color:var(--brand);font-weight:700;font-size:64px;line-height:66px}
.forms{left:520px;top:115px;width:355px;height:350px;background:linear-gradient(135deg,#f4f7fb,#b9cde4);border-radius:6px;transform:rotate(-4deg)}
.readmore{left:862px;top:402px;width:243px;height:62px;border-radius:8px;background:linear-gradient(var(--blue-light),var(--blue-dark));color:#fff;font-size:21px;display:flex;align-items:center;justify-content:center;gap:10px}
.readmore .arrow{width:36px;height:36px;border-radius:50%;background:#fff;display:flex;align-items:center;justify-content:center}

.band{left:0;top:485px;width:1200px;height:175px;background:linear-gradient(#e9eaed,var(--band))}
.card{top:518px;width:232px;height:118px;border-radius:8px;background:linear-gradient(#ffe887,var(--yellow-deep));border:1px solid #d99d00;padding:16px 0 0 20px}
.card h3{font-size:28px;font-weight:400;line-height:29px;color:var(--ink)}
.card p{font-size:15px;color:var(--ink);margin-top:2px}
.card svg{position:absolute;right:12px;top:10px}

.newsletter{left:90px;top:690px;width:250px;height:215px;border-radius:8px;background:linear-gradient(var(--blue-light),var(--blue-dark));padding:14px 18px}
.newsletter h2{font-size:27px;color:var(--orange);font-weight:700;background:#eef2f7;border-radius:6px;padding:8px 12px;margin:0 -6px 0 16px}
.newsletter label{display:block;color:#fff;font-size:14px;margin-top:22px}
.newsletter .field{height:24px;background:#fff;border:1px solid #9fb9d8;margin-top:8px}
.newsletter .subscribe{margin:18px 0 0 104px;width:110px;height:26px;border-radius:13px;background:linear-gradient(#ffe36e,var(--yellow-deep));font-size:14px;color:#6a4a00;display:flex;align-items:center;justify-content:center}

.why{left:374px;top:686px;font-size:28px;color:var(--orange);font-weight:700}
.point{width:345px;display:flex;gap:20px}
.point .icon{width:68px;height:68px;flex:none;border-radius:8px;background:linear-gradient(#fafafa,#dadde2);border:1px solid #c8ccd2;display:flex;align-items:center;justify-content:center}
.point p{font-size:12.5px;line-height:17px;color:var(--muted)}

.footer{left:0;top:928px;width:1200px;height:81px;background:linear-gradient(var(--blue-light),var(--blue-dark));color:#fff;text-align:center}
.footer .links{font-size:12px;margin-top:20px}
.footer .links span{margin:0 4px}
.footer .copy{font-size:12px;margin-top:18px}
</style>
</head>
<body>
<div class="abs topbar"></div>
<div class="abs follow">Follow Us : <span class="social"></span><span class="social"></span><span class="social"></span><span class="social"></span></div>
<div class="abs callus">
  <svg width="22" height="22" viewBox="0 0 24 24"><path d="M6 2l4 4-2 3c1 3 4 6 7 7l3-2 4 4-3 4C10 21 3 14 2 5z" fill="#f0961c"/></svg>
  Call Us Now : <span class="num">(000) 000-0000</span>
</div>

<nav class="abs nav">
  <a class="active" href="#">Home Insurance</a><a href="#">About Us</a><a href="#">Broker Area</a><a href="#">Leave a comment</a><a href="#">Life Insurance</a><a href="#">Over 50 Life Insurance No Medicals</a><a href="#">Contact Us</a>
</nav>

<section class="abs hero"></section>
<div class="abs mascot" role="img" aria-label="Mascot illustration of the brand character"></div>
<div class="abs brand">Velvet<br>Lantern</div>
<div class="abs forms" role="img" aria-label="Illustration of stacked application forms"></div>
<div class="abs readmore">Click to Read More <span class="arrow"><svg width="18" height="18" viewBox="0 0 18 18"><path d="M4 9h9M9 4l5 5-5 5" stroke="#1d5796" stroke-width="3" fill="none"/></svg></span></div>

<div class="abs band"></div>
<div class="abs card" style="left:90px"><h3>Life<br>Insurance</h3><p>Know more about it</p>
  <svg width="60" height="60" viewBox="0 0 60 60"><path d="M5 30a25 25 0 0 1 50 0z" fill="#ffad1f"/><path d="M30 30v20a5 5 0 0 1-10 0" stroke="#8a5a00" stroke-width="3" fill="none"/></svg></div>
<div class="abs card" style="left:347px"><h3>Broker<br>Area</h3><p>Know more about it</p>
  <svg width="60" height="60" viewBox="0 0 60 60"><rect x="6" y="14" width="48" height="36" rx="3" fill="#ffb21c"/><rect x="6" y="8" width="20" height="10" rx="2" fill="#ffb21c"/></svg></div>
<div class="abs card" style="left:611px"><h3>Home<br>Insurance</h3><p>Know more about it</p>
  <svg width="60" height="60" viewBox="0 0 60 60"><path d="M6 30L30 8l24 22h-7v22H13V30z" fill="#ffb21c"/><rect x="25" y="36" width="10" height="16" fill="#fff3c4"/></svg></div>
<div class="abs card" style="left:870px"><h3>Over 50<br>Life Insurance</h3><p>Know more about it</p>
  <svg width="40" height="40" viewBox="0 0 40 40"><path d="M15 4h10v11h11v10H25v11H15V25H4V15h11z" fill="#ffb21c"/></svg></div>

<aside class="abs newsletter">
  <h2>Our Newsletter</h2>
  <label>Enter your email address:</label>
  <div class="field"></div>
  <div class="subscribe">Subscribe »</div>
</aside>

<h2 class="abs why">Why Pick Velvet Lantern?</h2>
<div class="abs point" style="left:380px;top:730px">
  <div class="icon"><svg width="46" height="46" viewBox="0 0 46 46"><circle cx="23" cy="23" r="19" fill="#3b8ad6"/><path d="M23 23V4a19 19 0 0 1 19 19z" fill="#f0961c"/><path d="M23 23h19a19 19 0 0 1-8 15z" fill="#7cc144"/></svg></div>
  <p>Velvet Lantern works as an intermediary between clients who are looking into products such as life insurance and the IFA and Brokerage community who can assist them.</p>
</div>
<div class="abs point" style="left:380px;top:825px">
  <div class="icon"><svg width="46" height="46" viewBox="0 0 46 46"><circle cx="23" cy="23" r="19" fill="#2c6fb4"/><path d="M16 12l16 10-7 2 5 9-4 2-5-9-5 5z" fill="#fff"/></svg></div>
  <p>We have teamed up with some of the countries largest survey companies and respond directly to customers who have suggested they may be interested in learning more.</p>
</div>
<div class="abs point" style="left:750px;top:730px">
  <div class="icon"><svg width="46" height="46" viewBox="0 0 46 46"><rect x="6" y="26" width="8" height="14" fill="#3b8ad6"/><rect x="19" y="16" width="8" height="24" fill="#f0961c"/><rect x="32" y="8" width="8" height="32" fill="#7cc144"/></svg></div>
  <p>Each brokerage has its own set of criteria and parameters for customers, for example IFA companies who like to advise clients need the customers to have enough</p>
</div>
<div class="abs point" style="left:750px;top:825px">
  <div class="icon"><svg width="46" height="46" viewBox="0 0 46 46"><rect x="8" y="6" width="30" height="36" rx="4" fill="#f0961c"/><rect x="12" y="10" width="22" height="8" fill="#fff"/><g fill="#fff"><rect x="12" y="22" width="6" height="5"/><rect x="20" y="22" width="6" height="5"/><rect x="28" y="22" width="6" height="5"/><rect x="12" y="31" width="6" height="5"/><rect x="20" y="31" width="6" height="5"/><rect x="28" y="31" width="6" height="5"/></g></svg></div>
  <p>General knowledge about life insurance and how it operates is limited within what the industry terms “the insurance gap” and our aim is to ensure our customers understand</p>
</div>

<footer class="abs footer">
  <div class="links">Home Insurance<span>|</span>About Us<span>|</span>Broker Area<span>|</span>Leave a Comment<span>|</span>Life Insurance<span>|</span>Over 50 Life Insurance No Medicals<span>|</span>Contact Us</div>
  <div class="copy">© Copyright 2011 VelvetLantern. All Rights Reserved.</div>
</footer>
</body>
</html>
```